Local Food Manufacturing needs label design for sweetened cocoa

We are a local food manufacturing company in the Philippines that caters to the lower class market for chocolate drinks. Our products are mainly powder-based.
Most powdered drinks here are 3-in-1 with chocolate (cocoa), milk and sugar. For the product, we made it 2-in-1 with only chocolate (cocoa) and sugar.
This product now caters to three markets: the "champorado" market, baking market and also the drinking market. We try to focus on "champorado" and the baking market.
Champorado is a local dish that is basically chocolate porridge; chocolate (cocoa powder) mixed with wet rice. A lot of bakeries here use chocolate powder for baking needs. Search the internet for an idea of champorado.

We don't have any color preference so it is up to you to match it with the market.
We would like to see a transparent area in the label for consumers to see the powder inside.

Product name: Mang Lito Sweetened Cocoa 200g
Label size: 280mm x 175mm
Please see attached files for samples of our product line so that you'll have an idea. We also uploaded a sweetened cocoa design that is too similar with our other products that we didn't consider using it.

Feel free to leave a message for clarifications.

Font styles to use
Sans Serif

Colors

Designer to choose colors to be used in the design.

Requirements
Must have
• Mang Lito brand
Nice to have
• Cocoa tablets
Should not have
• any design with milk

```html
<!DOCTYPE html>
<html lang="en">
<head>
<meta charset="utf-8">
<title>Mang Lito Sweetened Cocoa 200g – Label Concept</title>
<link href="https://fonts.googleapis.com/css2?family=Oswald:wght@500;600&family=Cinzel:wght@600&display=swap" rel="stylesheet">
<style>
  :root {
    --black: #000000;
    --panel: #1a0f0a;
    --orange: #f0622a;
    --gold: #e3a54c;
    --cream: #fbedcd;
    --white: #ffffff;
    --window: #5b3a2d;
    --ring-dark: #1b120c;
  }
  html, body { margin: 0; padding: 0; overflow: hidden; background: var(--black); }
  .canvas {
    position: relative;
    width: 1200px;
    height: 1000px;
    overflow: hidden;
    background: var(--black);
    font-family: "Oswald", "Arial Narrow", sans-serif;
  }
  .label-art { position: absolute; left: 0; top: 0; }
  .brand-name {
    font-family: "Oswald", "Arial Narrow", sans-serif;
    font-weight: 600;
    fill: var(--cream);
    letter-spacing: 2px;
  }
  .ring-text {
    font-family: "Cinzel", serif;
    font-weight: 600;
    font-size: 40px;
    fill: var(--ring-dark);
    letter-spacing: 6px;
  }
  .band-text {
    font-family: "Oswald", "Arial Narrow", sans-serif;
    font-weight: 500;
    fill: var(--cream);
    text-anchor: middle;
  }
  .net-weight {
    font-family: "Oswald", "Arial Narrow", sans-serif;
    font-weight: 500;
    fill: var(--panel);
    text-anchor: middle;
  }
  .headline {
    position: absolute;
    left: 778px;
    top: 138px;
    width: 360px;
    margin: 0;
    text-align: center;
    color: var(--white);
    font-weight: 500;
    font-size: 56px;
    line-height: 66px;
    letter-spacing: 0;
    white-space: nowrap;
  }
  .headline .amp {
    display: flex;
    align-items: center;
    justify-content: center;
    gap: 14px;
    height: 62px;
  }
  .headline .amp::before, .headline .amp::after {
    content: "";
    width: 96px;
    height: 2px;
    background: linear-gradient(to right, transparent, var(--white));
  }
  .headline .amp::after { background: linear-gradient(to left, transparent, var(--white)); }
  .palette {
    position: absolute;
    left: 858px;
    top: 586px;
    width: 200px;
    margin: 0;
    padding: 0;
    list-style: none;
    text-align: center;
    color: var(--white);
    font-size: 36px;
    font-weight: 500;
    line-height: 48px;
  }
  .palette li { height: 108px; }
  .swatch {
    display: block;
    width: 96px;
    height: 26px;
    margin: 0 auto 6px;
    border: 3px solid var(--white);
    border-radius: 50%;
  }
  .swatch--orange { background: var(--orange); }
  .swatch--gold { background: var(--gold); }
  .swatch--black { background: var(--black); }
</style>
</head>
<body>
<main class="canvas">
  <svg class="label-art" width="760" height="1000" viewBox="0 0 760 1000" aria-label="Mang Lito Sweetened Cocoa 200g label">
    <defs>
      <radialGradient id="panelGlow" cx="0.3" cy="0.72" r="0.7">
        <stop offset="0" stop-color="#d9561c"/>
        <stop offset="0.35" stop-color="#6b2a10"/>
        <stop offset="1" stop-color="#140b07"/>
      </radialGradient>
      <linearGradient id="titleTone" x1="0" y1="0" x2="0" y2="1">
        <stop offset="0" stop-color="#f7ead2"/>
        <stop offset="1" stop-color="#e6c48c"/>
      </linearGradient>
      <path id="ringTop" d="M 330 700 A 185 185 0 0 1 700 700"/>
      <path id="ringBottom" d="M 318 700 A 197 197 0 0 0 712 700"/>
    </defs>

    <g class="label-frame">
      <rect x="36" y="36" width="674" height="1020" rx="46" fill="var(--gold)"/>
      <rect x="44" y="44" width="658" height="1004" rx="40" fill="var(--orange)"/>
      <rect x="50" y="50" width="646" height="992" rx="36" fill="var(--black)"/>
      <rect x="60" y="60" width="626" height="972" rx="30" fill="url(#panelGlow)"/>
      <rect x="66" y="66" width="614" height="960" rx="26" fill="none" stroke="var(--gold)" stroke-width="3"/>
    </g>

    <g class="brand-lockup">
      <circle cx="210" cy="165" r="44" fill="var(--orange)"/>
      <rect x="250" y="138" width="336" height="70" rx="10" fill="var(--orange)"/>
      <text class="brand-name" x="418" y="194" font-size="50" text-anchor="middle">MANG LITO</text>
    </g>

    <rect class="title-lettering" x="115" y="220" width="470" height="370" rx="30" fill="url(#titleTone)" opacity="0.9"
          role="img" aria-label="Hand-lettered product title: Sweetened Cocoa"/>

    <g class="uses-band">
      <polygon points="95,658 322,600 322,1000 95,1000" fill="var(--orange)"/>
      <text class="band-text" x="208" y="695" font-size="36">Great</text>
      <text class="band-text" x="208" y="735" font-size="36">for baking</text>
      <line x1="130" y1="752" x2="286" y2="752" stroke="var(--cream)" stroke-width="2"/>
      <text class="band-text" x="208" y="800" font-size="36">Perfect</text>
      <line x1="130" y1="828" x2="172" y2="828" stroke="var(--cream)" stroke-width="2"/>
      <text class="band-text" x="208" y="840" font-size="36">for</text>
      <line x1="244" y1="828" x2="286" y2="828" stroke="var(--cream)" stroke-width="2"/>
      <text class="band-text" x="208" y="878" font-size="36">champorado</text>
      <text class="net-weight" x="215" y="958" font-size="36">200 g</text>
    </g>

    <g class="quality-seal">
      <circle cx="515" cy="700" r="222" fill="var(--gold)" stroke="var(--ring-dark)" stroke-width="3"/>
      <circle cx="515" cy="700" r="212" fill="none" stroke="var(--ring-dark)" stroke-width="2"/>
      <circle cx="515" cy="700" r="152" fill="none" stroke="var(--ring-dark)" stroke-width="3"/>
      <text class="ring-text"><textPath href="#ringTop" startOffset="50%" text-anchor="middle">PREMIUM</textPath></text>
      <text class="ring-text"><textPath href="#ringBottom" startOffset="50%" text-anchor="middle">QUALITY</textPath></text>
      <rect x="318" y="590" width="52" height="200" rx="26" fill="#b98236" role="img" aria-label="Cocoa pod and leaves illustration"/>
      <rect x="660" y="590" width="52" height="200" rx="26" fill="#b98236" role="img" aria-label="Cocoa pod and leaves illustration"/>
      <circle class="product-window" cx="515" cy="700" r="136" fill="var(--window)" stroke="var(--ring-dark)" stroke-width="6"/>
    </g>
  </svg>

  <h1 class="headline">
    MANG LITO<br>GETS<br>CLEAN<span class="amp">&amp;</span>PREMIUM<br>STYLE
  </h1>

  <ul class="palette">
    <li><span class="swatch swatch--orange"></span>Orange</li>
    <li><span class="swatch swatch--gold"></span>Gold</li>
    <li><span class="swatch swatch--black"></span>Black</li>
  </ul>
</main>
</body>
</html>
```